Website Widget/Code Snippet Website

We create a number of website plugins (called widgets) for a website builder called LumaSite. It is a library of widgets that users who design their site in LumaSite can use on their website.
I am looking for a new design for this site;
https://www.quillpatchbay.net
The website is going to official launch so I would like a new, clean design that emphasizes the huge library of widgets for LumaSite.
Tag Line: LumaSiteOrchard Makes Anything Possible
We should emphasize the Sign Up option which provides a subscription to access the widgets.
I would like;
1. A home page
2. A widgets page which shows all the available widgets
3. A pricing/signup page
4. Widget information page
One overall simplistic design that is easy to navigate
Industry/Entity Type
Website building and website design
Number of Pages Required
4 page
Look and feel

```html
<!DOCTYPE html>
<html lang="en">
<head>
<meta charset="utf-8">
<title>LumaSiteOrchard – Widgets for LumaSite</title>
<link href="https://fonts.googleapis.com/css2?family=Montserrat:wght@500;600;700;800&family=Mulish:wght@400;600;700&display=swap" rel="stylesheet">
<style>
:root{
  --blue:#1fb7ee;
  --blue-dark:#0e9fd6;
  --blue-soft:#e8f7fd;
  --ink:#1d2330;
  --muted:#7a8494;
  --faint:#b8c0cc;
  --line:#e6ebf1;
  --white:#ffffff;
  --page:#ffffff;
}
*{box-sizing:border-box;margin:0;padding:0}
html,body{width:1200px;height:3348px;overflow:hidden}
body{font-family:"Mulish",sans-serif;color:var(--ink);background:var(--page);position:relative}
.h-font{font-family:"Montserrat",sans-serif}
.btn{display:inline-block;background:var(--blue);color:var(--white);font:700 13px "Montserrat",sans-serif;border-radius:4px;padding:11px 22px;text-decoration:none}
.btn-outline{background:var(--white);color:var(--blue);border:2px solid var(--blue)}

/* header + hero */
.hero{position:absolute;top:0;left:0;width:1200px;height:720px;background:linear-gradient(180deg,#f3fbff 0%,#e9f7fd 100%)}
.site-header{position:absolute;top:0;left:0;width:1200px;height:84px;display:flex;align-items:center;padding:0 128px;justify-content:space-between}
.brand{display:flex;align-items:center;gap:10px;font:700 28px "Montserrat",sans-serif;color:var(--ink)}
.brand-square{width:26px;height:26px;background:var(--blue);border-radius:5px}
.nav{display:flex;align-items:center;gap:30px;font:600 14px "Montserrat",sans-serif}
.nav a{color:var(--ink);text-decoration:none}
.nav a.active{color:var(--blue)}
.nav .btn{padding:9px 16px;font-size:12px}
.hero-copy{position:absolute;left:128px;top:226px;width:460px}
.hero-copy h1{font:800 28px/1.35 "Montserrat",sans-serif;text-transform:uppercase;letter-spacing:.3px}
.hero-copy .btn{margin-top:42px}
.hero-art{position:absolute;left:590px;top:140px;width:500px;height:500px;border-radius:40px;background:radial-gradient(circle at 70% 30%,#2cc3f5 0%,#9fdcf3 45%,#e6f5fb 80%)}

/* feature band */
.features{position:absolute;top:640px;left:0;width:1200px;height:220px;background:var(--blue);clip-path:polygon(0 35%,100% 0,100% 100%,0 100%)}
.feature-row{position:absolute;top:700px;left:130px;width:940px;display:flex;color:var(--white)}
.feature{flex:1;text-align:center;font:600 14px "Montserrat",sans-serif;border-right:1px solid rgba(255,255,255,.4);padding:14px 0}
.feature:last-child{border-right:none}
.feature svg{display:block;margin:0 auto 14px}

/* section title */
.section-title{position:absolute;left:50%;transform:translateX(-50%);border:2px solid var(--blue);padding:10px 20px;font:800 15px "Montserrat",sans-serif;text-transform:uppercase;letter-spacing:1px;background:var(--white)}

/* widgets */
.widget-grid{position:absolute;top:984px;left:160px;width:880px;display:grid;grid-template-columns:repeat(4,202px);column-gap:24px;row-gap:30px}
.widget-card{height:336px;background:var(--white);border-radius:6px;box-shadow:0 4px 22px rgba(30,60,90,.12);text-align:center;padding:40px 18px 0}
.widget-thumb{width:72px;height:72px;border-radius:14px;margin:0 auto 28px}
.widget-card h3{font:600 14px "Montserrat",sans-serif;margin-bottom:10px}
.widget-card p{font-size:11px;line-height:1.5;color:var(--muted);height:50px}
.widget-card .btn{padding:7px 14px;font-size:10px;margin-top:14px}
.view-all{position:absolute;top:1752px;left:516px;width:168px;text-align:center;padding:9px 0}

/* stats */
.stats{position:absolute;top:1848px;left:0;width:1200px;height:168px;background:var(--blue-soft);display:flex;justify-content:center;gap:0;padding-top:46px}
.stat{width:225px;text-align:center}
.stat b{display:block;font:600 34px "Montserrat",sans-serif;color:var(--blue)}
.stat span{font-size:12px;color:var(--ink)}

/* plans */
.plans-intro{position:absolute;top:2170px;left:0;width:1200px;text-align:center;font-size:14px;color:var(--muted)}
.plans{position:absolute;top:2222px;left:128px;width:944px;display:flex;gap:44px;align-items:flex-start}
.plan{flex:1;background:var(--white);box-shadow:0 4px 26px rgba(30,60,90,.13);border-radius:4px;overflow:hidden;margin-top:22px}
.plan.pro{margin-top:0}
.plan-head{background:var(--blue);color:var(--white);text-align:center;padding:26px 0 26px}
.plan.pro .plan-head{padding:26px 0 30px}
.plan-head h3{font:700 19px "Montserrat",sans-serif}
.plan-head small{display:block;font-size:10px;opacity:.85;margin:4px 0 16px}
.price{display:flex;justify-content:center;align-items:center;gap:8px;font:700 34px "Montserrat",sans-serif}
.price em{font:700 9px "Montserrat",sans-serif;font-style:normal;background:var(--white);color:var(--blue);padding:4px 8px;border-radius:3px}
.plan ul{list-style:none;padding:20px 26px 10px}
.plan li{font-size:13px;padding:13px 0;border-bottom:1px solid var(--line);display:flex;gap:10px;align-items:center}
.plan li.off{color:var(--faint);padding-left:22px}
.plan li svg{flex:none}
.plan .btn{display:block;width:106px;margin:22px auto 30px;text-align:center;padding:10px 0}

/* newsletter */
.newsletter{position:absolute;top:2800px;left:0;width:1200px;height:280px;background:linear-gradient(100deg,#d8f1fb 0%,#f4fbfe 50%,#ffffff 100%)}
.newsletter .section-title{top:36px}
.newsletter p{position:absolute;top:108px;width:1200px;text-align:center;font-size:13px;color:var(--muted)}
.signup{position:absolute;top:160px;left:320px;width:560px;height:48px;display:flex;border:1px solid var(--line);background:var(--white);border-radius:4px}
.signup span{flex:1;padding:15px 20px;font-size:12px;color:var(--muted)}
.signup .btn{border-radius:0 4px 4px 0;padding:15px 30px}

/* footer */
.site-footer{position:absolute;top:3080px;left:0;width:1200px;height:268px;background:var(--blue);color:var(--white)}
.site-footer .brand{position:absolute;left:128px;top:96px;color:var(--white);font-size:30px}
.site-footer .brand-square{background:var(--white)}
.foot-col{position:absolute;top:46px;font-size:11px;line-height:1.9}
.foot-col h4{font:700 11px "Montserrat",sans-serif;margin-bottom:6px;text-transform:uppercase}
.socials{display:flex;gap:8px;margin-top:4px}
.socials i{width:26px;height:26px;background:var(--white);border-radius:4px;display:block}
.copyright{position:absolute;bottom:22px;width:1200px;text-align:center;font-size:10px;opacity:.85}
</style>
</head>
<body>

<section class="hero">
  <header class="site-header">
    <div class="brand"><span class="brand-square"></span>LumaSiteOrchard</div>
    <nav class="nav">
      <a class="active" href="#">Home</a><a href="#">Widgets</a><a href="#">Pricing</a><a href="#">Blog</a><a href="#">Contact</a>
      <svg width="18" height="18" viewBox="0 0 18 18" fill="none" stroke="#1d2330" stroke-width="2"><circle cx="7.5" cy="7.5" r="5.5"/><path d="M12 12l5 5"/></svg>
      <a class="btn" href="#">See All Widgets</a>
    </nav>
  </header>
  <div class="hero-copy">
    <h1>We provide additional widgets for LumaSite – easy to use, advanced site builder for Slate.</h1>
    <a class="btn" href="#">Sign Up For Free</a>
  </div>
  <div class="hero-art" role="img" aria-label="Cluster of rounded widget app icons"></div>
</section>

<div class="features"></div>
<div class="feature-row">
  <div class="feature"><svg width="36" height="36" viewBox="0 0 36 36" fill="none" stroke="#fff" stroke-width="2"><rect x="3" y="3" width="12" height="12" rx="2"/><rect x="21" y="3" width="12" height="12" rx="2"/><rect x="3" y="21" width="12" height="12" rx="2"/><circle cx="27" cy="27" r="6"/></svg>All widgets in one service</div>
  <div class="feature"><svg width="36" height="36" viewBox="0 0 36 36" fill="none" stroke="#fff" stroke-width="2"><circle cx="18" cy="18" r="15"/><text x="18" y="22" fill="#fff" stroke="none" font-size="9" font-family="Montserrat,sans-serif" font-weight="700" text-anchor="middle">FREE</text></svg>Free</div>
  <div class="feature"><svg width="36" height="36" viewBox="0 0 36 36" fill="none" stroke="#fff" stroke-width="2"><circle cx="18" cy="18" r="6"/><path d="M18 3v6M18 27v6M3 18h6M27 18h6M7 7l4 4M25 25l4 4M7 29l4-4M25 11l4-4"/></svg>Easy to install</div>
  <div class="feature"><svg width="36" height="36" viewBox="0 0 36 36" fill="none" stroke="#fff" stroke-width="2"><path d="M4 28a14 14 0 0 1 28 0"/><path d="M18 28l8-10"/></svg>Speed up your website</div>
</div>

<h2 class="section-title" style="top:884px">Widgets</h2>
<div class="widget-grid">
  <article class="widget-card"><div class="widget-thumb" role="img" aria-label="Floating navigation bar icon" style="background:linear-gradient(135deg,#31c2f4,#0c8fd0)"></div><h3>Floating Navigation Bar</h3><p>Keep your menu in view as visitors scroll down any page.</p><a class="btn" href="#">Read More</a></article>
  <article class="widget-card"><div class="widget-thumb" role="img" aria-label="Nav bar with icons graphic" style="background:linear-gradient(135deg,#f4d23c,#6fc35a)"></div><h3>Nav Bar with Icons</h3><p>Add small icons beside each menu item for a clear layout.</p><a class="btn" href="#">Read More</a></article>
  <article class="widget-card"><div class="widget-thumb" role="img" aria-label="Typed text graphic" style="background:linear-gradient(135deg,#ffe9a8,#f5a623)"></div><h3>Typed</h3><p>Display animated typed text lines.</p><a class="btn" href="#">Read More</a></article>
  <article class="widget-card"><div class="widget-thumb" role="img" aria-label="Website notification graphic" style="background:linear-gradient(135deg,#3b6fe0,#e8453c)"></div><h3>Website Notification</h3><p>Add a short alert bar to tell visitors about news.</p><a class="btn" href="#">Read More</a></article>
  <article class="widget-card"><div class="widget-thumb" role="img" aria-label="Search list graphic" style="background:linear-gradient(135deg,#4a7cf0,#1740b8)"></div><h3>Search List</h3><p>Let people filter long lists on your site.</p><a class="btn" href="#">Read More</a></article>
  <article class="widget-card"><div class="widget-thumb" role="img" aria-label="Typewriter effect graphic" style="background:linear-gradient(135deg,#d7dcff,#9aa6e8)"></div><h3>Typewriter Effect</h3><p>Show your text as if it was typed.</p><a class="btn" href="#">Read More</a></article>
  <article class="widget-card"><div class="widget-thumb" role="img" aria-label="Flipbook graphic" style="background:linear-gradient(135deg,#1f5fc4,#f0a93a)"></div><h3>Flipbook</h3><p>Create a realistic page-turning book.</p><a class="btn" href="#">Read More</a></article>
  <article class="widget-card"><div class="widget-thumb" role="img" aria-label="Special offer bar graphic" style="background:linear-gradient(135deg,#f5c431,#e4572e)"></div><h3>Special Offer Bar</h3><p>Add a promotion banner to your website.</p><a class="btn" href="#">Read More</a></article>
</div>
<a class="btn btn-outline view-all" href="#">View All Widgets</a>

<section class="stats">
  <div class="stat"><b>156</b><span>Widgets Installed Today</span></div>
  <div class="stat"><b>12.9M+</b><span>Daily Widget Impressions</span></div>
  <div class="stat"><b>165K+</b><span>Daily Widget Clicks</span></div>
  <div class="stat"><b>15.0%</b><span>Avg. Follower Boost</span></div>
</section>

<h2 class="section-title" style="top:2072px">Our Plans</h2>
<p class="plans-intro">Choose one of our plans below to gain access to our widgets, support and custom widget development.</p>
<div class="plans">
  <div class="plan">
    <div class="plan-head"><h3>Standard</h3><small>Start with our most basic widgets</small><div class="price">$49 <em>PER YEAR</em></div></div>
    <ul>
      <li><svg width="12" height="12" viewBox="0 0 12 12"><path d="M1 6l3 3 7-7" fill="none" stroke="#1fb7ee" stroke-width="2"/></svg>All Standard Widgets</li>
      <li><svg width="12" height="12" viewBox="0 0 12 12"><path d="M1 6l3 3 7-7" fill="none" stroke="#1fb7ee" stroke-width="2"/></svg>Email Support</li>
      <li class="off">Premium Widgets</li>
      <li class="off">Custom Development</li>
    </ul>
    <a class="btn" href="#">Purchase</a>
  </div>
  <div class="plan">
    <div class="plan-head"><h3>Advanced</h3><small>Unlock all premium widgets today</small><div class="price">$69 <em>PER YEAR</em></div></div>
    <ul>
      <li><svg width="12" height="12" viewBox="0 0 12 12"><path d="M1 6l3 3 7-7" fill="none" stroke="#1fb7ee" stroke-width="2"/></svg>All Standard Widgets</li>
      <li><svg width="12" height="12" viewBox="0 0 12 12"><path d="M1 6l3 3 7-7" fill="none" stroke="#1fb7ee" stroke-width="2"/></svg>Premium widgets</li>
      <li><svg width="12" height="12" viewBox="0 0 12 12"><path d="M1 6l3 3 7-7" fill="none" stroke="#1fb7ee" stroke-width="2"/></svg>Priority email support</li>
      <li class="off">Custom Development</li>
    </ul>
    <a class="btn" href="#">Purchase</a>
  </div>
  <div class="plan pro">
    <div class="plan-head"><h3>Pro</h3><small>Access to all the widgets</small><div class="price">$149.95 <em>PER YEAR</em></div></div>
    <ul>
      <li><svg width="12" height="12" viewBox="0 0 12 12"><path d="M1 6l3 3 7-7" fill="none" stroke="#1fb7ee" stroke-width="2"/></svg>All Standard Widgets</li>
      <li><svg width="12" height="12" viewBox="0 0 12 12"><path d="M1 6l3 3 7-7" fill="none" stroke="#1fb7ee" stroke-width="2"/></svg>All Premium Widgets</li>
      <li><svg width="12" height="12" viewBox="0 0 12 12"><path d="M1 6l3 3 7-7" fill="none" stroke="#1fb7ee" stroke-width="2"/></svg>Priority Support</li>
      <li><svg width="12" height="12" viewBox="0 0 12 12"><path d="M1 6l3 3 7-7" fill="none" stroke="#1fb7ee" stroke-width="2"/></svg>Priority Feature Dev</li>
      <li><svg width="12" height="12" viewBox="0 0 12 12"><path d="M1 6l3 3 7-7" fill="none" stroke="#1fb7ee" stroke-width="2"/></svg>Custom Development</li>
      <li><svg width="12" height="12" viewBox="0 0 12 12"><path d="M1 6l3 3 7-7" fill="none" stroke="#1fb7ee" stroke-width="2"/></svg>Early Widget Access</li>
    </ul>
    <a class="btn" href="#">Purchase</a>
  </div>
</div>

<section class="newsletter">
  <h2 class="section-title">Join Our Newsletter</h2>
  <p>Sign up to our newsletter and get free access to all of our widgets while we are in beta.</p>
  <div class="signup"><span>Email Address</span><a class="btn" href="#">Subscribe</a></div>
</section>

<footer class="site-footer">
  <div class="brand"><span class="brand-square"></span>LumaSiteOrchard</div>
  <div class="foot-col" style="left:530px"><h4>Quick Links</h4>Home<br>Widgets<br>Pricing<br>Blog<br>Contact</div>
  <div class="foot-col" style="left:700px"><h4>Highlighted Widgets</h4>Floating Navigation Bar<br>Advanced Image Gallery<br>E-Book Flipbook<br>Popup On Scroll</div>
  <div class="foot-col" style="left:950px"><h4>Follow Us</h4><div class="socials"><i></i><i></i><i></i></div></div>
  <div class="copyright">Copyright © 2024. All Rights Reserved.</div>
</footer>

</body>
</html>
```